Business Card Design Project - IT Company

CLOUD IT company working with medium to large corporate clients requires 2 sided Business Card design.

Strong, Professional and modern is what I am looking for.

The Logo JPG attached has all the colour palette options. which consist of Red and Silver on various backgrounds

Preferred option for the Back of card is either Silver Text on Red or Silver Text on Black. Though this is not concrete. Surprise me.

Logo must be prominent along with Contact details of the staff member

Tagline can be all Capitals " CLOUD MANAGED SERVICES"

I will look to provide feedback and tweaks to get the right design so it should be a fun process.

I will provide the layered files to the top few contenders.

Reason: Leaving the door open for some creativity. Don't forget this is an technology company. .

Target Market(s)

Leaders, decision makers, CEOs, CIOs,

Industry/Entity Type

Business

Requirements
Must have
• Data must have is

Company Name: Brelquist
Tagline: Cloud Managed Services

No Particular order

First Name Last name
Director
Mobile 0477 555 019
www.brelquist-example.com
First.Lastname@brelquist-example.com
Suite 7, 48 Wexmoor Lane, Sydney NSW 2000

```html
<!DOCTYPE html>
<html lang="en">
<head>
<meta charset="utf-8">
<title>Brelquist Business Card</title>
<link rel="stylesheet" href="https://fonts.googleapis.com/css2?family=Open+Sans:wght@400;600;700;800&display=swap">
<style>
  :root {
    --backdrop: #2b2b2b;
    --card-white: #f4f4f4;
    --card-black: #050505;
    --ink: #2a2a2a;
    --ink-soft: #4a4a4a;
    --brand-red: #9e1b1f;
    --silver: #c9c9c9;
    --silver-light: #e6e6e6;
  }
  * { margin: 0; padding: 0; box-sizing: border-box; }
  html, body {
    width: 1200px;
    height: 900px;
    overflow: hidden;
    background: var(--backdrop);
    font-family: "Open Sans", Arial, sans-serif;
  }
  .canvas {
    position: relative;
    width: 1200px;
    height: 900px;
    display: flex;
    align-items: center;
    justify-content: center;
    gap: 60px;
  }
  .card {
    position: relative;
    width: 500px;
    height: 286px;
    border-radius: 2px;
    box-shadow: 0 14px 30px rgba(0,0,0,0.45);
    overflow: hidden;
  }

  /* Front: contact side */
  .card--front {
    background: var(--card-white);
    color: var(--ink);
  }
  .brand-lockup {
    position: absolute;
    display: flex;
    align-items: center;
  }
  .card--front .brand-lockup {
    top: 30px;
    left: 130px;
    gap: 12px;
  }
  .brand-mark {
    border-radius: 50%;
    flex: none;
  }
  .card--front .brand-mark {
    width: 30px;
    height: 30px;
    background: var(--brand-red);
  }
  .brand-text {
    display: flex;
    flex-direction: column;
    align-items: flex-end;
  }
  .brand-name {
    font-weight: 800;
    line-height: 1;
  }
  .card--front .brand-name {
    font-size: 38px;
    color: var(--ink);
  }
  .tagline {
    font-weight: 700;
    text-transform: uppercase;
    letter-spacing: 0.02em;
  }
  .card--front .tagline {
    font-size: 9.5px;
    color: var(--ink);
    margin-top: 2px;
  }
  .contact {
    position: absolute;
    left: 40px;
    top: 118px;
    padding-left: 14px;
    border-left: 1.5px solid var(--brand-red);
    font-size: 13px;
    line-height: 1.45;
    color: var(--ink-soft);
  }
  .contact__name {
    font-size: 15px;
    letter-spacing: 0.03em;
    color: var(--ink);
    text-transform: uppercase;
  }
  .contact__role { margin-bottom: 2px; }
  .contact__label {
    display: inline-block;
    width: 16px;
    font-weight: 700;
    color: var(--brand-red);
  }
  .website {
    position: absolute;
    left: 40px;
    bottom: 22px;
    font-size: 13px;
    font-weight: 700;
    color: var(--ink);
  }
  .website__name { color: var(--brand-red); }

  /* Back: brand side */
  .card--back {
    background: var(--card-black);
  }
  .card--back .brand-lockup {
    top: 92px;
    left: 36px;
    gap: 20px;
  }
  .card--back .brand-mark {
    width: 58px;
    height: 58px;
    background: var(--silver);
  }
  .card--back .brand-name {
    font-size: 80px;
    color: var(--silver-light);
  }
  .card--back .tagline {
    font-size: 17px;
    color: var(--silver);
    margin-top: 2px;
  }
</style>
</head>
<body>
<main class="canvas">
  <section class="card card--front" aria-label="Business card front">
    <div class="brand-lockup">
      <span class="brand-mark" aria-hidden="true"></span>
      <div class="brand-text">
        <span class="brand-name">Brelquist</span>
        <span class="tagline">Cloud Managed Services</span>
      </div>
    </div>
    <div class="contact">
      <p class="contact__name">Maren Holloway</p>
      <p class="contact__role">Director</p>
      <p><span class="contact__label">M</span>0477 555 019</p>
      <p><span class="contact__label">E</span>First.Lastname@brelquist-example.com</p>
      <p>Suite 7, 48 Wexmoor Lane, Sydney NSW 2000</p>
    </div>
    <p class="website">www.<span class="website__name">brelquist-example</span>.com</p>
  </section>

  <section class="card card--back" aria-label="Business card back">
    <div class="brand-lockup">
      <span class="brand-mark" aria-hidden="true"></span>
      <div class="brand-text">
        <span class="brand-name">Brelquist</span>
        <span class="tagline">Cloud Managed Services</span>
      </div>
    </div>
  </section>
</main>
</body>
</html>
```